Werbe-Email-Design
Zielgruppe
Wir sind Dienstleister in der Industrie/ Automobilindustrie. Die Zielgruppe für unsere Werbe-Email sind potenzielle Kunden (möglichst Einkäufer) für unser Produkt (Motorhersteller für DC-Motoren). Da es sich um eine Werbe-Email handelt, soll beim Öffnen möglichst gleich ersichtlich sein, ob das Produkt für den Empfänger brauchbar ist, sodass er in diesem Falle die 'nervige Werbe-Mail' nicht sofort löscht.
Aufgabenstellung
Bei dem 'Newsletter' soll es sich um eine einmalige Werbemail handeln, durch die potenzielle Kunden auf unser Produkt aufmerksam werden und mit uns in Kontakt treten, unsere Website besuchen oder sofort bestellen.
Das Produkt verfolgt einen eher ungewöhnlichen Ansatz, der den potenziellen Kunden eben ansprechen könnte oder nicht, da er damit selbst ein umfangreicheres Produkt anbieten könnte, sollte das in seinem Interesse sein.
Da dies ein neuer Ansatz für den potenziellen Kunden wäre, wird der Empfänger der Email nicht damit rechnen. Deshalb ist wichtig, dass beim Öffnen der Email sofort klar wird, was unser Produkt bietet und wie es unserem Kunden von Nutzen sein kann.
Es handelt sich bei den potenziellen Kunden um Motorhersteller (für DC-Motoren im Fahrzeug, bspw. Fensterheber), die diesen Motor selbst nicht ansteuern. Sie verkaufen diese Motoren also entweder ohne Steuerung oder kaufen die Steuerung von einem Dienstleister. Wir bieten eben diese Steuerung an, allerdings konfigurierbar auf die Anwendung des Kunden, sodass kein weiterer Entwicklungsaufwand entsteht. Der Kunde kann also entweder einen bestehenden Lieferanten für seine Steuerung durch uns ersetzen, da wir in der Lage sind, einen sehr niedrigen Stückpreis zu bieten, oder sein Geschäftsfeld erweitern.
Durch die Email soll sich der Empfänger um diesen Umstand und die Vorteile, die durch unser Produkt für ihn entstehen, bewusstwerden.
Beim Öffnen der Email soll der 'Eye-Catcher'-Bereich zu sehen sein, der den Kunden neugierig machen soll. Hat der Kunde Interesse, soll bei Scrollen mehr Information zu sehen sein.
Dieser 'Eye-Catcher'-Bereich ist in der anhängenden PowerPoint-Datei auf der ersten Seite enthalten. Beim Scrollen sollen die Informationen, die sich auf den nächsten Seiten befinden, zu sehen sein. Des Weiteren soll ein Foto der geöffneten ECU (anhängend) zu sehen sein, mit den Informationen zum Gehäuse, sowie zwei Screenshots der mitgelieferten GUI. Da ..

```html
<!DOCTYPE html>
<html lang="de">
<head>
<meta charset="utf-8">
<title>ECU Werbe-Email – Vogt Steuerungstechnik</title>
<link href="https://fonts.googleapis.com/css2?family=Lato:wght@400;700&family=Poppins:wght@300;400;500&display=swap" rel="stylesheet">
<style>
  :root {
    --orange: #ff9a22;
    --orange-deep: #ff9500;
    --orange-text: #f7931e;
    --blue: #0a2bc4;
    --white: #ffffff;
    --ink: #1a1a1a;
    --rule: #c9c9c9;
  }
  * { box-sizing: border-box; margin: 0; padding: 0; }
  html, body { width: 723px; height: 1200px; overflow: hidden; }
  body {
    position: relative;
    font-family: "Lato", sans-serif;
    color: var(--ink);
    background: linear-gradient(to bottom, var(--white) 0 115px, var(--orange) 115px 720px, var(--orange-deep) 720px);
  }
  .brand {
    position: absolute; top: 0; left: 0; width: 723px; height: 115px;
    display: flex; align-items: center; justify-content: center; gap: 10px;
  }
  .brand-dot { width: 14px; height: 14px; border-radius: 50%; background: var(--orange-text); }
  .brand-name { font-family: "Lato", sans-serif; font-weight: 700; font-size: 24px; color: #222; }

  .card {
    position: absolute; background: var(--white); border-radius: 7px;
    font-size: 11px; line-height: 21px;
  }
  .card-left { left: 14px; top: 155px; width: 235px; height: 398px; padding: 22px 14px 0 24px; }
  .card-right { left: 474px; top: 155px; width: 235px; height: 398px; padding: 22px 14px 0 18px; }
  .card-title {
    color: var(--orange-text); font-weight: 700; font-size: 14.5px; line-height: 20px;
    text-align: center; letter-spacing: .3px;
  }
  .card-rule { width: 92px; height: 1px; background: var(--rule); margin: 10px auto 12px; }
  .card-right .card-rule { background: var(--orange-text); }
  .feature-list { list-style: none; }
  .feature-list > li { position: relative; padding-left: 13px; }
  .feature-list > li::before {
    content: ""; position: absolute; left: 0; top: 8px; width: 4px; height: 4px;
    border-radius: 50%; background: var(--orange-text);
  }
  .sub-list { list-style: none; }
  .sub-list li { position: relative; padding-left: 14px; }
  .sub-list li::before {
    content: ""; position: absolute; left: 0; top: 7px; width: 4px; height: 4px;
    border-radius: 50%; border: 1px solid var(--orange-text);
  }

  .card-highlight {
    position: absolute; left: 246px; top: 145px; width: 231px; height: 417px;
    background: var(--blue); color: var(--white); padding: 26px 14px 0 16px;
    box-shadow: 0 4px 12px rgba(0,0,0,.25);
    font-size: 11px; line-height: 20.8px;
  }
  .card-highlight .card-title { color: var(--white); }
  .card-highlight .card-rule { background: var(--white); width: 108px; }
  .card-highlight .feature-list > li::before { background: var(--white); }
  .card-highlight b { font-weight: 700; }

  .applications {
    position: absolute; left: 20px; top: 580px; width: 683px;
    font-family: "Poppins", sans-serif; font-weight: 500; font-size: 14.3px; line-height: 24px;
    color: var(--white); text-align: center;
  }

  .scope {
    position: absolute; left: 14px; top: 674px; width: 695px; height: 127px;
    background: var(--blue); border-radius: 6px;
    display: grid; grid-template-columns: 313px 1fr; padding: 24px 0 0 33px; row-gap: 5px;
    font-family: "Poppins", sans-serif; font-weight: 500; font-size: 14.3px; color: var(--white);
    align-content: start;
  }
  .scope-item { display: flex; align-items: center; gap: 10px; height: 22px; }
  .scope-item svg { width: 12px; height: 10px; flex: none; }

  .details {
    position: absolute; left: 14px; top: 815px; width: 695px; height: 371px;
    background: var(--white); border-radius: 7px; padding: 22px 20px 0 34px;
    font-family: "Poppins", sans-serif; font-weight: 300; font-size: 12.6px; line-height: 21.7px;
  }
  .details-title { font-weight: 400; color: var(--orange-text); font-size: 16px; line-height: 24px; margin-bottom: 2px; }
  .details-title + .detail-list { margin-top: 0; }
  .detail-list { list-style: none; margin-left: -20px; }
  .detail-list li { position: relative; padding-left: 20px; }
  .detail-list li::before {
    content: ""; position: absolute; left: 2px; top: 9px; width: 4px; height: 4px;
    border-radius: 50%; background: var(--orange-text);
  }
  .details-title.second { margin-top: 17px; }
</style>
</head>
<body>
  <header class="brand">
    <span class="brand-dot"></span>
    <span class="brand-name">Vogt Steuerungstechnik</span>
  </header>

  <section class="card card-left">
    <h2 class="card-title">TECHNISCHE<br>VORTEILE</h2>
    <div class="card-rule"></div>
    <ul class="feature-list">
      <li>Dank Halbleitertechnologie gegenüber Relais:
        <ul class="sub-list">
          <li>Leiser</li>
          <li>Kein Verschleiß (Kontaktprellen, Lichtbogenentwicklung), kein Icing</li>
          <li>Sehr präzises Ansprechverhalten</li>
        </ul>
      </li>
      <li>Hohe Dynamik im Lastbereich: bis 19A (Stromspitzen bis 30A)</li>
      <li>Geringer Stromverbrauch:
        <ul class="sub-list">
          <li>Sleep-Mode: &lt; 100 µA.</li>
          <li>On-Mode: &lt; 100 mA</li>
        </ul>
      </li>
      <li>Robust gegen Umwelteinflüsse</li>
    </ul>
  </section>

  <section class="card card-right">
    <h2 class="card-title">STRATEGISCHE<br>VORTEILE</h2>
    <div class="card-rule"></div>
    <ul class="feature-list">
      <li>Komplettpaket zur Ermittlung Ihrer Systemparameter (Strom-/ Spannungsschwellen, Timingparameter u.v.m.)</li>
      <li>ECU bewährt seit 2010</li>
      <li>HW-Stand 3. Generation</li>
      <li>Zertifiziert nach …</li>
      <li>Keine Basisentwicklung erforderlich</li>
      <li>Minimaler Aufwand bei Applikation durch GUI-Konfigurator</li>
      <li>Made in Germany</li>
      <li>Schneller geht’s nicht</li>
    </ul>
  </section>

  <section class="card-highlight">
    <h2 class="card-title">IN WENIGEN TAGEN<br>ZUR FERTIGEN</h2>
    <div class="card-rule"></div>
    <ul class="feature-list">
      <li>Ermitteln Sie Ihre Systemparameter mit unserem <b>Komplettpaket</b> zum Anschluss an <b>Ihren DC-Motor</b></li>
      <li>Per einfachem Mausklick werden Ihre Parameter in unsere <b>fertige Software</b> geladen</li>
      <li>Sie können Ihre Einstellungen innerhalb <b>weniger Minuten testen</b>, bis Sie mit unserer maßgeschneiderten Lösung zufrieden sind</li>
      <li>Wir erstellen das <b>LIN File</b> für Ihre Kommunikation mit dem System Ihres Kunden</li>
      <li>Die <b>fertige ECU</b> ist bereit für Ihre Bestellung</li>
    </ul>
  </section>

  <p class="applications">Fensterheber | elektrisch verstellbare Spiegel | Schiebedach | elektrische Sitzverstellung | Scheibenwischer&nbsp; Waschwasserpumpen | Türverriegelung | Spoilerverstellung | Beschattungssysteme | elektrischer Heckklappenantrieb</p>

  <section class="scope">
    <div class="scope-item"><svg viewBox="0 0 12 10"><path d="M1 5.5 4.3 8.5 11 1.5" fill="none" stroke="#fff" stroke-width="2.2"/></svg>Anwendung</div>
    <div class="scope-item"><svg viewBox="0 0 12 10"><path d="M1 5.5 4.3 8.5 11 1.5" fill="none" stroke="#fff" stroke-width="2.2"/></svg>bei hohem Lastbereich</div>
    <div class="scope-item"><svg viewBox="0 0 12 10"><path d="M1 5.5 4.3 8.5 11 1.5" fill="none" stroke="#fff" stroke-width="2.2"/></svg>für DC Bürstenmotoren</div>
    <div class="scope-item"><svg viewBox="0 0 12 10"><path d="M1 5.5 4.3 8.5 11 1.5" fill="none" stroke="#fff" stroke-width="2.2"/></svg>mit schnellen Schaltzeiten</div>
    <div class="scope-item"><svg viewBox="0 0 12 10"><path d="M1 5.5 4.3 8.5 11 1.5" fill="none" stroke="#fff" stroke-width="2.2"/></svg>in einer LIN-Umgebung</div>
    <div class="scope-item"><svg viewBox="0 0 12 10"><path d="M1 5.5 4.3 8.5 11 1.5" fill="none" stroke="#fff" stroke-width="2.2"/></svg>präzisen Positionsinformationen.</div>
  </section>

  <section class="details">
    <h3 class="details-title">Mit unserer ECU sparen Sie Kosten, da</h3>
    <ul class="detail-list">
      <li>wir aufgrund eines langjährigen Skaleneffekts einen niedrigen Stückpreis anbieten</li>
      <li>Keine Entwicklungskosten entstehen</li>
      <li>für Sie kaum Aufwand bei der Konfiguration entsteht – unser Entwicklungstool mit Realtime Strom- und Spannungsmessung erleichtert die schnelle Applikation</li>
      <li>Sie von uns ein kostenloses Konfigurationspaket zur Verfügung gestellt bekommen – es fallen für Sie bis zur Bestellung keine Kosten an!</li>
    </ul>
    <h3 class="details-title second">Gehäuse</h3>
    <ul class="detail-list">
      <li>12-poliger KTX-Stecker</li>
      <li>2-Komponenten Vergusstechnologie auf Silikonbasis</li>
      <li>IP53</li>
      <li>Material: PA6-GF15</li>
      <li>Einfaches Clip-System zur Befestigung</li>
      <li>Alternatives Gehäuse auf Anfrage</li>
    </ul>
  </section>
</body>
</html>
```